Brain Science Music company needs modern clean website

We're looking for a website that's very clean and modern but also has some nice bold (futuristic) colors in it. The design should communicate a company that's providing something new and fresh! We'd greatly appreciate web designs similar to: https://thebrightfolio.co/

Lumen Cascade is a US-based Neuroscience music company that offers state-of-the-art technology solutions that help people focus, relax and sleep with the help of scientifically engineered music.

Target Market(s)

US businesses looking for specialized neuroscience music technology.

Logo Text

LumenCascade or LC

Coding

Coded - Design and coding required

Number of Pages Required

1 page

Font styles to use
Sans Serif

Colors

Designer to choose colors to be used in the design.

Requirements
Nice to have
• A website similar to: https://thebrightfolio.co/
We like the colors, the fonts, the simple design layouts and the colorful images.

```html
<!DOCTYPE html>
<html lang="en">
<head>
<meta charset="utf-8">
<title>Lumen Cascade — The new frontier of music and the brain</title>
<link href="https://fonts.googleapis.com/css2?family=Lato:ital,wght@0,400;0,700;0,900;1,400&display=swap" rel="stylesheet">
<style>
:root{
  --ink:#1f1f2b;
  --muted:#5c5c6a;
  --violet:#5b4fd6;
  --violet-deep:#4338b8;
  --violet-soft:#9d96ee;
  --rose:#e83a5a;
  --rose-soft:#f4a3b3;
  --sun:#f6c94b;
  --sun-soft:#fbe3a0;
  --mint:#6edcc4;
  --mint-soft:#bdeee3;
  --mist:#f5f5fb;
  --white:#ffffff;
}
*{box-sizing:border-box;margin:0;padding:0}
html,body{width:1200px;height:4894px;overflow:hidden}
body{font-family:"Lato",sans-serif;color:var(--ink);background:var(--white);position:relative}
.abs{position:absolute}
.btn-outline{position:absolute;display:inline-flex;align-items:center;justify-content:center;border:2px solid var(--rose);color:var(--rose);border-radius:32px;font-weight:700;font-size:17px;text-transform:uppercase;background:transparent}
h1,h2{font-weight:900;line-height:1.18}
.section-title{font-size:50px;font-weight:700;line-height:1.25}

/* header */
.brand{left:108px;top:28px}
.brand-name{font-size:33px;font-weight:900}
.brand-tag{font-size:17px;margin-top:4px}
.callus{left:880px;top:14px;color:var(--white);font-size:17px;display:flex;align-items:center;gap:8px}
.nav{left:676px;top:58px;display:flex;gap:26px;color:var(--white);font-size:18px;font-weight:700}

/* hero */
.hero-blob{left:0;top:0}
.hero-art{left:600px;top:150px;width:560px;height:680px;border-radius:280px 280px 140px 140px;background:linear-gradient(180deg,rgba(255,255,255,.22),rgba(255,255,255,.05))}
.hero-title{left:108px;top:145px;font-size:66px}
.hero-lead{left:110px;top:478px;font-size:22px;line-height:1.6;color:var(--muted);width:380px}
.hero-cta{left:111px;top:584px;width:194px;height:62px}
.hero-arrow{left:112px;top:710px}

/* pillars */
.pillars-title{left:0;width:1200px;top:885px;text-align:center}
.pillar{position:absolute;top:1040px;width:200px;text-align:center}
.pillar-icon{position:relative;width:170px;height:160px;margin:0 auto}
.pillar-icon .halo{position:absolute;left:0;top:8px;width:158px;height:150px;border-radius:50%}
.pillar-icon .disc{position:absolute;left:10px;top:0;width:158px;height:150px;border-radius:50%;display:flex;align-items:center;justify-content:center}
.pillar-label{margin-top:26px;font-size:25px;font-weight:700;color:#3a3a46}

/* welcome */
.welcome-bg{left:0;top:1310px}
.welcome-title{left:110px;top:1410px}
.body-copy{font-size:15.5px;line-height:1.8;color:var(--muted)}
.welcome-p1{left:110px;top:1558px;width:460px}
.welcome-p2{left:110px;top:1640px;width:460px}
.welcome-cta{left:111px;top:1780px;width:170px;height:58px}
.video{left:606px;top:1450px;width:482px;height:317px;border-radius:10px;background:radial-gradient(circle at 50% 50%,#15307a 0,#0a1240 35%,#040820 70%);box-shadow:0 14px 30px rgba(0,0,0,.18);display:flex;align-items:center;justify-content:center}

/* why */
.why-art{left:60px;top:2050px;width:450px;height:450px;border-radius:225px 225px 0 0;background:radial-gradient(circle at 50% 45%,#e7a0dc 0,#c977d8 40%,#eadcf3 70%,rgba(255,255,255,0) 72%)}
.why-title{left:585px;top:1998px}
.why-list{left:586px;top:2150px;width:520px;list-style:none}
.why-list li{position:relative;padding-left:28px;font-size:15.5px;line-height:1.8;color:var(--muted);margin-bottom:26px}
.why-list li svg{position:absolute;left:0;top:6px}
.why-cta{left:585px;top:2491px;width:170px;height:58px}

/* tech */
.tech-title{left:110px;top:2640px}
.tech-copy{left:110px;top:2782px;width:520px}
.mini-row{left:110px;top:2897px;display:flex;gap:22px;align-items:center}
.mini{display:flex;align-items:center;gap:12px;font-size:21px;color:#2b2b36}
.mini-dot{width:72px;height:72px;border-radius:50%;display:flex;align-items:center;justify-content:center}
.tech-cta{left:111px;top:3015px;width:170px;height:58px}
.tech-art{left:503px;top:2600px}

/* story */
.story-bg{left:0;top:3180px}
.story-photo{left:110px;top:3282px;width:430px;height:430px;border-radius:50%;background:linear-gradient(160deg,#c9c6d6,#7c7f93 55%,#2e3350)}
.story-title{left:602px;top:3290px;color:var(--white);font-size:52px;font-weight:700}
.story-sub{left:602px;top:3362px;color:var(--white);font-size:22px;font-weight:700}
.story-copy{left:602px;width:500px;color:#e6e4fb;font-size:15.5px;line-height:1.7}
.story-cta{left:603px;top:3660px;width:170px;height:54px}

/* testimonials */
.quote-shadow{left:92px;top:3905px;width:600px;height:190px;background:var(--violet);transform:rotate(-4deg);border-radius:10px}
.quote-card{left:112px;top:3875px;width:606px;height:196px;background:var(--rose);border-radius:10px;color:var(--white)}
.avatar{left:152px;top:3828px;width:104px;height:104px;border-radius:50%;background:linear-gradient(#dcdcdc,#a8a8a8);border:5px solid var(--white)}
.quote-name{left:273px;top:3897px;color:var(--white);font-size:20px;font-weight:700}
.quote-text{left:152px;top:3952px;width:480px;color:var(--white);font-style:italic;font-size:18px;line-height:1.65}
.testi-title{left:792px;top:3872px}
.testi-nav{left:792px;top:4004px;display:flex;gap:6px}
.circle-btn{width:52px;height:52px;border-radius:50%;border:1px solid #e6e6ee;background:var(--white);display:flex;align-items:center;justify-content:center;box-shadow:0 3px 8px rgba(0,0,0,.06)}

/* cta */
.cta-wave{left:0;top:4150px}
.cta-title{left:0;width:1200px;top:4248px;text-align:center;font-size:52px;font-weight:700}
.cta-sub{left:0;width:1200px;top:4328px;text-align:center;font-size:22px;color:#444}
.cta-btn{left:497px;top:4396px;width:208px;height:66px;font-size:20px}
.divider{left:110px;top:4480px;width:980px;height:1px;background:#e3e3ea}

/* footer */
.foot-brand{left:108px;top:4552px}
.foot-brand .brand-name{font-size:35px}
.foot-brand .brand-tag{font-size:19px;margin-top:8px}
.foot-head{font-size:20px;font-weight:700}
.foot-links{left:509px;top:4543px}
.foot-links ul{list-style:none;margin-top:14px}
.foot-links li{font-size:16px;color:var(--muted);line-height:1.75}
.newsletter{left:697px;top:4543px;width:384px}
.newsletter p{font-size:16px;color:var(--muted);line-height:1.7;margin-top:14px}
.email{margin-top:14px;height:50px;border:1px solid #dedee6;border-radius:4px;padding:0 16px;display:flex;align-items:center;color:#666;font-size:16px}
.signup{left:697px;top:4720px;width:124px;height:46px;font-size:16px}
.bottom-bar{left:0;top:4806px;width:1200px;height:88px;background:var(--violet)}
.copyright{left:110px;top:4838px;color:var(--white);font-size:17px}
.social{left:955px;top:4828px;display:flex;gap:10px}
.social span{width:38px;height:38px;border-radius:50%;border:1.5px solid rgba(255,255,255,.8)}
</style>
</head>
<body>

<svg class="abs hero-blob" width="1200" height="840" viewBox="0 0 1200 840" aria-hidden="true">
  <path d="M700 0 H1200 V780 C1080 790 980 805 880 790 C720 770 560 720 515 560 C475 420 500 300 560 190 C610 100 660 40 700 0Z" fill="#4436c4"/>
  <path d="M725 0 H1200 V760 C1090 770 990 780 895 765 C745 745 600 700 560 550 C525 420 545 300 605 195 C650 110 690 45 725 0Z" fill="var(--violet)"/>
</svg>

<header>
  <div class="abs brand"><div class="brand-name">Lumen Cascade</div><div class="brand-tag">The new frontier of music and the brain</div></div>
  <div class="abs callus">
    <svg width="16" height="16" viewBox="0 0 24 24" aria-hidden="true"><path d="M6.6 10.8a15 15 0 006.6 6.6l2.2-2.2c.3-.3.7-.4 1-.2 1.1.4 2.3.6 3.6.6.6 0 1 .4 1 1V20c0 .6-.4 1-1 1A17 17 0 013 4c0-.6.4-1 1-1h3.5c.6 0 1 .4 1 1 0 1.2.2 2.4.6 3.6.1.3 0 .7-.2 1z" fill="#fff"/></svg>
    Call us on: 1 555 010 2040
  </div>
  <nav class="abs nav"><span>About</span><span>Solutions</span><span>Science</span><span>Resources</span><span>Contact</span></nav>
</header>

<section class="hero">
  <div class="abs hero-art" role="img" aria-label="Illustration of a woman meditating cross-legged while listening to music on headphones, surrounded by floating music notes"></div>
  <h1 class="abs hero-title">The New<br>Frontier of<br>Music and<br>the Brain</h1>
  <p class="abs hero-lead">Merging neuroscience and music, creating audio enhancing.</p>
  <a class="btn-outline hero-cta">Get more info</a>
  <svg class="abs hero-arrow" width="22" height="42" viewBox="0 0 22 42" aria-hidden="true"><path d="M11 2V38M3 30L11 38 19 30" stroke="#888" stroke-width="3" fill="none"/></svg>
</section>

<section class="pillars">
  <h2 class="abs section-title pillars-title">Merging neuroscience and music,<br>creating audio enhancing</h2>
  <div class="pillar" style="left:112px">
    <div class="pillar-icon"><span class="halo" style="background:var(--violet-soft)"></span><span class="disc" style="background:var(--violet)">
      <svg width="64" height="70" viewBox="0 0 64 70" aria-label="Lightbulb icon" role="img"><path d="M32 6C20 6 12 15 12 26c0 8 4 13 8 17 2 2 3 5 3 8h18c0-3 1-6 3-8 4-4 8-9 8-17C52 15 44 6 32 6Z" fill="none" stroke="#fff" stroke-width="3"/><path d="M24 57H40M26 64H38M32 20v14M25 27h14" stroke="#fff" stroke-width="3" stroke-linecap="round"/></svg>
    </span></div>
    <div class="pillar-label">Productivity</div>
  </div>
  <div class="pillar" style="left:371px">
    <div class="pillar-icon"><span class="halo" style="background:var(--sun-soft)"></span><span class="disc" style="background:var(--sun)">
      <svg width="70" height="70" viewBox="0 0 70 70" aria-label="Moon and sleep icon" role="img"><path d="M36 10A26 26 0 1060 44 20 20 0 0136 10Z" fill="none" stroke="#fff" stroke-width="3.5" stroke-linejoin="round"/><path d="M40 20h10l-10 12h10M52 6h8l-8 9h8" stroke="#fff" stroke-width="3" fill="none" stroke-linejoin="round"/></svg>
    </span></div>
    <div class="pillar-label">Sleep</div>
  </div>
  <div class="pillar" style="left:630px">
    <div class="pillar-icon"><span class="halo" style="background:var(--rose-soft)"></span><span class="disc" style="background:var(--rose)">
      <svg width="70" height="66" viewBox="0 0 70 66" aria-label="Headphones icon" role="img"><path d="M10 42V34a25 25 0 0150 0v8" fill="none" stroke="#fff" stroke-width="3.5"/><rect x="6" y="38" width="13" height="22" rx="5" fill="none" stroke="#fff" stroke-width="3.5"/><rect x="51" y="38" width="13" height="22" rx="5" fill="none" stroke="#fff" stroke-width="3.5"/></svg>
    </span></div>
    <div class="pillar-label">Meditation</div>
  </div>
  <div class="pillar" style="left:889px">
    <div class="pillar-icon"><span class="halo" style="background:var(--mint-soft)"></span><span class="disc" style="background:var(--mint)">
      <svg width="72" height="60" viewBox="0 0 72 60" aria-label="Pulse line icon" role="img"><path d="M4 32h14l6-14 10 30 8-22 5 6h21" fill="none" stroke="#fff" stroke-width="3.5" stroke-linejoin="round" stroke-linecap="round"/></svg>
    </span></div>
    <div class="pillar-label">Athletics</div>
  </div>
</section>

<section class="welcome">
  <svg class="abs welcome-bg" width="1200" height="600" viewBox="0 0 1200 600" aria-hidden="true">
    <path d="M0 70 C300 -20 800 10 1200 90 V600 H0Z" fill="var(--mist)"/>
    <path d="M0 70 C300 -20 800 10 1200 90" stroke="#ebebf3" stroke-width="10" fill="none"/>
  </svg>
  <h2 class="abs section-title welcome-title">Welcome to<br>Lumen Cascade</h2>
  <p class="abs body-copy welcome-p1">Nemo enim ipsam voluptatem quia voluptas sit aspernatur aut odit aut fugit, sed quia conse.</p>
  <p class="abs body-copy welcome-p2">Aiuuntur magni dolores eos qui ratione voluptatem sequi nesciunt. Neque porro quisquam est, qui dolorem ipsum quia dolor sit amet, consectetur, adipisci velit, sed qui numquam eius modi tempora incidunt ut lab.</p>
  <a class="btn-outline welcome-cta">Read more</a>
  <div class="abs video" role="img" aria-label="Video still of a glowing blue brain over a sound wave">
    <svg width="40" height="44" viewBox="0 0 40 44" aria-hidden="true"><path d="M6 4L36 22 6 40Z" fill="#fff"/></svg>
  </div>
</section>

<section class="why">
  <div class="abs why-art" role="img" aria-label="Illustration of a head silhouette with a glowing brain inside soft purple circles and floating music notes"></div>
  <h2 class="abs section-title why-title">Why Choose<br>Lumen Cascade</h2>
  <ul class="abs why-list">
    <li><svg width="16" height="16" viewBox="0 0 16 16" aria-hidden="true"><circle cx="8" cy="8" r="8" fill="var(--violet)"/><path d="M4.5 8.2L7 10.5 11.5 5.8" stroke="#fff" stroke-width="2" fill="none"/></svg>Neurons in our brains communicate with each other, forming thoughts, emotions, and ideas using electrical impulses.</li>
    <li><svg width="16" height="16" viewBox="0 0 16 16" aria-hidden="true"><circle cx="8" cy="8" r="8" fill="var(--violet)"/><path d="M4.5 8.2L7 10.5 11.5 5.8" stroke="#fff" stroke-width="2" fill="none"/></svg>Activities such as sleeping, working, or meditating, each have their own unique brainwave pattern.</li>
    <li><svg width="16" height="16" viewBox="0 0 16 16" aria-hidden="true"><circle cx="8" cy="8" r="8" fill="var(--violet)"/><path d="M4.5 8.2L7 10.5 11.5 5.8" stroke="#fff" stroke-width="2" fill="none"/></svg>Lumen Cascade leverages Musical Phase Locking, to optimize brainwave patterns for each desired activity.</li>
    <li><svg width="16" height="16" viewBox="0 0 16 16" aria-hidden="true"><circle cx="8" cy="8" r="8" fill="var(--violet)"/><path d="M4.5 8.2L7 10.5 11.5 5.8" stroke="#fff" stroke-width="2" fill="none"/></svg>Our music is driven by science. We utilize large scale studies &amp; data from electro-encephlograms to produce substantial results.</li>
  </ul>
  <a class="btn-outline why-cta">Read more</a>
</section>

<section class="tech">
  <svg class="abs tech-art" width="697" height="545" viewBox="0 0 697 545" role="img" aria-label="Illustration of a woman with headphones relaxing on cushions beside a large music player, with music notes and a cat">
    <defs><linearGradient id="techGrad" x1="0" y1="1" x2="1" y2="0"><stop offset="0" stop-color="#c99be8"/><stop offset=".5" stop-color="#9f9ef0"/><stop offset="1" stop-color="#b8d4f6"/></linearGradient></defs>
    <path d="M0 545 C10 470 80 420 170 390 C260 360 260 250 300 150 C340 60 440 0 560 10 C640 18 697 60 697 60 V545Z" fill="url(#techGrad)"/>
  </svg>
  <h2 class="abs section-title tech-title">State-of-the-art<br>Technology Solutions</h2>
  <p class="abs body-copy tech-copy">Lumen Cascade is a US-based Neuroscience music company that offers state-of-the-art technology solutions that help people focus, relax and sleep with the help of scientifically engineered music.</p>
  <div class="abs mini-row">
    <div class="mini"><div class="mini-dot" style="background:var(--violet)"><svg width="36" height="36" viewBox="0 0 36 36" role="img" aria-label="Focus icon"><circle cx="18" cy="18" r="15" fill="none" stroke="#fff" stroke-width="2.5"/><circle cx="18" cy="18" r="8" fill="none" stroke="#fff" stroke-width="2.5"/><circle cx="18" cy="18" r="2.5" fill="#fff"/></svg></div>Focus</div>
    <div class="mini"><div class="mini-dot" style="background:var(--mint)"><svg width="36" height="24" viewBox="0 0 36 24" role="img" aria-label="Relax icon"><path d="M2 8c5-6 9-6 14 0s9 6 14 0M2 18c5-6 9-6 14 0s9 6 14 0" fill="none" stroke="#fff" stroke-width="2.5" stroke-linecap="round"/></svg></div>Relax</div>
    <div class="mini"><div class="mini-dot" style="background:var(--sun)"><svg width="36" height="36" viewBox="0 0 36 36" role="img" aria-label="Sleep icon"><path d="M6 16h10L6 30h10M20 6h9l-9 11h9" fill="none" stroke="#fff" stroke-width="2.8" stroke-linejoin="round"/></svg></div>Sleep</div>
  </div>
  <a class="btn-outline tech-cta">Read more</a>
</section>

<section class="story">
  <svg class="abs story-bg" width="1200" height="605" viewBox="0 0 1200 605" aria-hidden="true">
    <defs><linearGradient id="storyGrad" x1="0" y1="0" x2="0" y2="1"><stop offset="0" stop-color="var(--violet)"/><stop offset="1" stop-color="var(--violet-deep)"/></linearGradient></defs>
    <path d="M0 60 C300 -10 800 0 1200 70 V605 H0Z" fill="url(#storyGrad)"/>
    <path d="M0 60 C300 -10 800 0 1200 70" stroke="#ececf4" stroke-width="10" fill="none"/>
  </svg>
  <div class="abs story-photo" role="img" aria-label="Portrait of the founder in a suit"></div>
  <h2 class="abs story-title">Owen’s Story</h2>
  <p class="abs story-sub">Founder and Team Leader of Lumen Cascade</p>
  <p class="abs story-copy" style="top:3412px">In conjunction with primary scientific advisor Dr. Harriet Vale. Owen is a pioneer in the neuroscience of music, and key innovator on the technology of Musical Phase Locking.</p>
  <p class="abs story-copy" style="top:3510px">At the age of 10, Owen wrote his first symphony and began studying music composition</p>
  <p class="abs story-copy" style="top:3582px">After exposure to alpha waves in music, Owen began a lifelong pursuit of merging neuroscience and music composition</p>
  <a class="btn-outline story-cta">Read more</a>
</section>

<section class="testimonials">
  <div class="abs quote-shadow"></div>
  <div class="abs quote-card"></div>
  <div class="abs avatar" role="img" aria-label="Client avatar placeholder"></div>
  <div class="abs quote-name">CALLUM</div>
  <svg class="abs" style="left:648px;top:3902px" width="48" height="40" viewBox="0 0 48 40" aria-hidden="true"><path d="M2 2H20V20L12 38H4L10 22H2Z M28 2H46V20L38 38H30L36 22H28Z" fill="#fff"/></svg>
  <p class="abs quote-text">Suuis aute irure dolor in reprehenderit in voluptate velit esse cillum dolore eu fugiat nulla pariatur. Excepteur sint occ aecat cupidatat.</p>
  <h2 class="abs section-title testi-title">Client<br>Testimonials</h2>
  <div class="abs testi-nav">
    <div class="circle-btn"><svg width="24" height="12" viewBox="0 0 24 12" aria-hidden="true"><path d="M22 6H3M8 1L3 6 8 11" stroke="var(--rose)" stroke-width="2" fill="none"/></svg></div>
    <div class="circle-btn"><svg width="24" height="12" viewBox="0 0 24 12" aria-hidden="true"><path d="M2 6H21M16 1L21 6 16 11" stroke="var(--rose)" stroke-width="2" fill="none"/></svg></div>
  </div>
</section>

<section class="cta">
  <svg class="abs cta-wave" width="1200" height="120" viewBox="0 0 1200 120" aria-hidden="true">
    <path d="M0 60 C300 10 800 20 1200 70" stroke="#f0f0f6" stroke-width="10" fill="none"/>
  </svg>
  <h2 class="abs cta-title">Want to know more?</h2>
  <p class="abs cta-sub">Let one of our trained team members help you</p>
  <a class="btn-outline cta-btn">Get a quote</a>
  <div class="abs divider"></div>
</section>

<footer>
  <div class="abs foot-brand"><div class="brand-name">Lumen Cascade</div><div class="brand-tag">The new frontier of music and the brain</div></div>
  <div class="abs foot-links">
    <div class="foot-head">Quick Links</div>
    <ul><li>About</li><li>Solutions</li><li>Science</li><li>Resources</li><li>Contact</li></ul>
  </div>
  <div class="abs newsletter">
    <div class="foot-head">Newsletter Sign Up</div>
    <p>Enter your email address to get<br>information about us</p>
    <div class="email">Email Address</div>
  </div>
  <a class="btn-outline signup">Sign up</a>
  <div class="abs bottom-bar"></div>
  <div class="abs copyright">Copyright © 2021, Lumen Cascade. All rights reserved.</div>
  <div class="abs social" aria-label="Social links"><span></span><span></span><span></span></div>
</footer>

</body>
</html>
```